One page (Bach and front) flyer graphic composition with all content provided

We need, by Sunday evening at the latest term, to have the enclosed page graphically worked. It will be inserted in a Fair Catalog. Dimensions 20x20We enclose logo and picture to include and draft. Don't consider the Power Point we include only to handle you content: take it from here and decide how to paste it in page to your own judgment.DLW is a software company, producing for investment market. image to give: SERIOUS, COMPETENT, STRAIGHT TO THE POINT and, most important, CREDIBLE company

Target Market(s)

Investors

Font styles to use
Serif

Colors
276eb1
0355a3
ffffff

Requirements
Must have
• Clear, strong Logo in the front page
• The picture on the back
Nice to have
• Credibility, space, clearness
Should not have
• Confusion, too much "loud"

```html
<!DOCTYPE html>
<html lang="en">
<head>
<meta charset="utf-8">
<title>DLW Fair Catalog Flyer — Front and Back</title>
<link rel="stylesheet" href="https://fonts.googleapis.com/css2?family=Montserrat:wght@300;400;500;600;700&display=swap">
<style>
  :root {
    --brand-blue: #155cd2;
    --accent-blue: #276eb1;
    --deep-blue: #0355a3;
    --white: #ffffff;
    --black: #000000;
    --ink: #1a1a1a;
    --rule: #c9c9c9;
    --page-bg: #e9e9e9;
  }
  * { box-sizing: border-box; margin: 0; padding: 0; }
  html, body {
    width: 1200px;
    height: 1200px;
    overflow: hidden;
    background: var(--page-bg);
    font-family: "Montserrat", sans-serif;
  }
  .canvas { position: relative; width: 1200px; height: 1200px; }

  .card { position: absolute; overflow: hidden; }

  /* Front */
  .card--front {
    left: 326px; top: 36px; width: 548px; height: 549px;
    background: var(--brand-blue);
    color: var(--white);
  }
  .front-disc {
    position: absolute;
    left: -118px; top: -36px;
    width: 480px; height: 480px;
    border-radius: 50%;
    background: var(--white);
  }
  .brand {
    position: absolute;
    display: flex; align-items: center; gap: 8px;
    font-weight: 600; line-height: 1;
  }
  .brand__dot { border-radius: 50%; flex: none; }
  .card--front .brand { right: 34px; top: 42px; font-size: 38px; color: var(--white); }
  .card--front .brand__dot { width: 34px; height: 34px; background: var(--white); }

  .tagline {
    position: absolute; right: 32px; top: 454px;
    font-size: 37px; font-weight: 400; letter-spacing: 0.5px; white-space: nowrap;
  }
  .tagline strong { font-weight: 700; }
  .front-url {
    position: absolute; right: 32px; top: 498px;
    font-size: 11px; letter-spacing: 5px;
  }

  /* Back */
  .card--back {
    left: 322px; top: 618px; width: 551px; height: 550px;
    background: var(--white);
  }
  .back-hero {
    position: absolute; left: 0; top: 0; width: 100%; height: 314px;
    background: var(--black); color: var(--white);
  }
  .hero-line1 {
    position: absolute; left: 36px; top: 118px;
    font-size: 29px; font-weight: 300; letter-spacing: 1px; white-space: nowrap;
  }
  .hero-line2 {
    position: absolute; left: 34px; top: 148px;
    font-size: 52px; font-weight: 300; letter-spacing: 1px; white-space: nowrap;
  }
  .hero-photo {
    position: absolute; left: 318px; top: 34px; width: 200px; height: 262px;
    background: radial-gradient(ellipse at 55% 35%, #8a7a52 0%, #3b3a30 38%, #111 72%, #000 100%);
  }
  .invite {
    position: absolute; left: 36px; top: 360px;
    font-size: 18px; line-height: 23px; color: var(--accent-blue); font-weight: 400;
  }
  .venue {
    position: absolute; left: 35px; top: 410px;
    font-size: 25px; color: var(--ink); font-weight: 400; white-space: nowrap;
  }
  .venue strong { color: var(--deep-blue); font-weight: 700; }
  .back-url {
    position: absolute; left: 36px; top: 505px;
    font-size: 11px; letter-spacing: 5px; color: var(--ink);
  }
  .back-rule {
    position: absolute; left: 36px; top: 520px; width: 374px; height: 1px;
    background: var(--rule);
  }
  .card--back .brand { right: 33px; top: 494px; font-size: 30px; color: var(--deep-blue); }
  .card--back .brand__dot { width: 27px; height: 27px; background: var(--deep-blue); }
</style>
</head>
<body>
<main class="canvas">
  <section class="card card--front" aria-label="Flyer front">
    <div class="front-disc"></div>
    <div class="brand"><span class="brand__dot"></span><span class="brand__name">DLW</span></div>
    <p class="tagline">Your Money <strong>Growth</strong></p>
    <p class="front-url">www.dlwinvest.example</p>
  </section>

  <section class="card card--back" aria-label="Flyer back">
    <div class="back-hero">
      <p class="hero-line1">WE ARE WAITING</p>
      <p class="hero-line2">FOR YOU!</p>
      <div class="hero-photo" role="img" aria-label="Photo of a martini glass filled with coins and ice cubes, with ice cubes at its base, on black"></div>
    </div>
    <p class="invite">Ask your invitation to our DLW Hostess<br>and be welcommed to:</p>
    <p class="venue">Presidential Suite <strong>Level 18</strong></p>
    <p class="back-url">www.dlwinvest.example</p>
    <div class="back-rule"></div>
    <div class="brand"><span class="brand__dot"></span><span class="brand__name">DLW</span></div>
  </section>
</main>
</body>
</html>
```